Wattle Creek Roadhouse Take-away Menu

Looking for a menu that is for a popular local roadhouse, we have fuel, take-away food, grocery's and local produce. Our target markets are locals, truck and bus drivers and holiday makers. I have attached logo and a layout mock up that I did and some menu lists

Target Market(s)

truck drivers, tourists, locals - 18-75 years, male and female, budget consious

Industry/Entity Type

Fast Food Restaurant

Colors
ec1f27
3176b5
33a6d7

Requirements
Must have
• Promote Off Road plenty of parking
• Promote Brolga Fuel including premium 98 Unleaded and Hi Flow Diesel
• Feature different headings of drinks menu, box specials, burgers and sandwiches, breakfast, fry up and opening hours
• Feature the logo,
• A5 folded landscape double sided
Nice to have
• I like the american roadhouse type style, easy to read, I like the rust, country, outback type themes
Should not have
• Fancy hard to read writing

```html
<!DOCTYPE html>
<html lang="en">
<head>
<meta charset="utf-8">
<title>Wattle Creek Roadhouse Take-away Menu</title>
<link rel="stylesheet" href="https://fonts.googleapis.com/css2?family=Roboto+Slab:wght@500;700;900&family=Bitter:ital,wght@1,700&family=Oswald:wght@500;700&family=Raleway:wght@500;700&display=swap">
<style>
:root{
  --stage:#d6d6d6;
  --kraft:#dccfb2;
  --kraft-dark:#cbbd9c;
  --ink:#262220;
  --blue:#3176b5;
  --sky:#33a6d7;
  --red:#ec1f27;
  --wood-1:#6e3a22;
  --wood-2:#9a5a36;
  --wood-3:#4e2816;
  --cream:#f3ead6;
  --band:#2b2b2b;
}
*{box-sizing:border-box;margin:0;padding:0}
html,body{width:1200px;height:960px;overflow:hidden;background:var(--stage)}
.spread{position:absolute;left:30px;top:60px;width:1140px;height:840px;display:flex;box-shadow:0 6px 20px rgba(0,0,0,.25)}
.panel{position:relative;width:570px;height:840px;background:var(--kraft)}
.panel--inside{border-right:1px solid var(--kraft-dark);display:flex;flex-direction:column;padding:40px 44px 32px 50px}

/* inside: drinks */
.menu{font-family:"Roboto Slab",serif;color:var(--ink)}
.ribbon{display:inline-block;background:var(--blue);color:#fff;font:900 24px "Roboto Slab",serif;letter-spacing:2px;padding:7px 34px;clip-path:polygon(0 0,100% 0,94% 50%,100% 100%,0 100%,6% 50%)}
.drinks{margin-top:16px;display:grid;grid-template-columns:1fr auto auto;column-gap:14px;align-items:start}
.item{font-weight:900;color:var(--blue);text-transform:uppercase;font-size:14px;line-height:1.2}
.note{font-weight:700;color:var(--ink);text-transform:none;font-size:12px;display:block}
.sizes{font-weight:900;color:var(--blue);font-size:14px;text-transform:uppercase;line-height:1.2;text-align:right}
.price{font-weight:900;color:var(--blue);font-size:14px;line-height:1.2;white-space:nowrap}
.row{display:flex;justify-content:space-between;gap:12px;margin-top:6px}
.fancy{margin-top:14px;display:flex;align-items:center;gap:14px}
.fancy__tag{background:#fff;color:var(--blue);font:900 16px "Roboto Slab",serif;text-transform:uppercase;padding:5px 26px;clip-path:polygon(0 0,100% 0,96% 50%,100% 100%,0 100%,4% 50%)}
.fancy__price{font:900 20px "Roboto Slab",serif;color:var(--blue)}
.served{font:700 italic 18px "Bitter",serif;margin:6px 0 2px 20px}
.shake{font-weight:700;font-size:13px;margin-left:60px;line-height:1.3}
.divider{height:2px;background:var(--red);margin:10px 0 8px;width:80%}
.board-call{font-weight:900;color:var(--blue);font-size:15px;text-transform:uppercase;line-height:1.2}
.goodies{font-weight:900;font-size:13px;text-transform:uppercase;line-height:1.35;margin-top:4px;text-align:center}
.bottom{margin-top:auto;display:flex;gap:22px;align-items:flex-end}
.map{flex:0 0 220px;height:150px;background:linear-gradient(135deg,#f4f2ec,#e3e0d6);border:4px solid #fff;box-shadow:0 1px 4px rgba(0,0,0,.2)}
.hours{flex:1;font-family:"Roboto Slab",serif;font-weight:700;font-size:12px;text-transform:uppercase;line-height:1.4;color:var(--ink)}
.hours h3{color:var(--red);font-weight:900;font-size:18px;line-height:1.2}
.hours dl{display:grid;grid-template-columns:auto auto;column-gap:10px;margin:4px 0 6px}
.hours dd{white-space:nowrap}

/* cover */
.frame{position:absolute;inset:22px;border:2px solid #6b6355}
.brand{position:absolute;left:0;right:0;top:70px;text-align:center;font-family:"Raleway",sans-serif;color:var(--ink)}
.brand__name{display:inline-flex;align-items:center;gap:12px;font:700 30px "Oswald",sans-serif;text-transform:uppercase;letter-spacing:2px}
.brand__dot{width:16px;height:16px;border-radius:50%;background:var(--ink)}
.brand__tags{display:flex;justify-content:center;gap:40px;margin-top:14px;font:700 13px "Raleway",sans-serif;text-transform:uppercase;letter-spacing:1px}
.brand__contact{display:flex;justify-content:space-between;padding:0 80px;margin-top:22px;font:500 14px "Raleway",sans-serif;letter-spacing:2px;text-transform:uppercase}
.boards{position:absolute;left:40px;right:40px;top:260px;height:380px}
.boards__wood{position:absolute;inset:0;background:repeating-linear-gradient(180deg,var(--wood-2) 0 70px,var(--wood-1) 70px 74px,var(--wood-3) 74px 76px),var(--wood-1)}
.sign{position:absolute;inset:40px 30px;border:1px solid rgba(243,234,214,.7);display:flex;flex-direction:column;align-items:center;justify-content:center;gap:12px;font:500 24px "Oswald",sans-serif;color:var(--cream);text-transform:uppercase;text-align:center;letter-spacing:1px;white-space:nowrap}
.parking{display:flex;align-items:center;margin:6px -50px;background:var(--band);color:#fff;font:700 28px "Oswald",sans-serif;padding:6px 40px;clip-path:polygon(0 0,100% 0,96% 50%,100% 100%,0 100%,4% 50%)}
.parking__of{background:var(--wood-2);margin:0 18px;padding:2px 16px;font-size:22px;clip-path:polygon(20% 0,80% 0,100% 50%,80% 100%,20% 100%,0 50%)}
.social{position:absolute;right:80px;bottom:70px;display:flex;align-items:center;gap:10px;font:500 16px "Raleway",sans-serif;letter-spacing:2px;text-transform:uppercase;color:var(--ink)}
.social__sq{width:14px;height:14px;background:var(--ink)}
</style>
</head>
<body>
<main class="spread">
  <section class="panel panel--inside">
    <div class="menu">
      <div class="ribbon">DRINKS MENU</div>
      <div class="drinks">
        <div class="item">Local Ridgeline Coffee<br>Kettle &amp; Fern Local Tea<span class="note">Earl grey, English breakfast, peppermint</span>Kettle &amp; Fern Wet Chai<span class="note">Brewed in soy milk</span></div>
        <div class="sizes">Small<br>Medium<br>Large</div>
        <div class="price">$3.50<br>$4.00<br>$4.50</div>
      </div>
      <div class="row"><div class="item">Milkshakes or thick shakes<span class="note">chocolate, banana, or strawberry, coffee</span></div><div class="price">$5.50</div></div>
      <div class="row"><div class="item">Morning sunrise juice<span class="note">Orange, pineapple, mint</span></div><div class="price">$5.50</div></div>
      <div class="row"><div class="item">Iced coffee &amp; iced chocolate</div><div class="price">$5.50</div></div>
      <div class="fancy"><span class="fancy__tag">Fancy Pants Shakes</span><span class="fancy__price">$9.50</span></div>
      <p class="served">Best served in house</p>
      <p class="shake">S'more sensation<br>Choc Crisp Kitty (contains coffee)<br>Chai and coconut made in heaven</p>
      <div class="divider"></div>
      <p class="board-call">Check the daily special board<br>for all sorts of goodies including</p>
      <p class="goodies">Homemade pies and sausage rolls<br>Moroccan chicken and plain meat lasagne<br>Fresh sushi<br>Banana bread, brownies, High Country cookies<br>and other sweet treats</p>
    </div>
    <div class="bottom">
      <div class="map" role="img" aria-label="Road map showing the roadhouse location near North Yarrow"></div>
      <div class="hours">
        <h3>Open 7 Days</h3>
        <dl><dt>Mon – Saturday:</dt><dd>7am – 6:30pm</dd><dt>Sunday:</dt><dd>7:30am – 5:30pm</dd></dl>
        <p>Please place dinner orders<br>before 5pm for pickup<br>between 5pm – 6:30pm</p>
        <p>We look forward to seeing you!</p>
      </div>
    </div>
  </section>

  <section class="panel panel--cover">
    <div class="frame"></div>
    <header class="brand">
      <div class="brand__name"><span class="brand__dot"></span>Wattle Creek Roadhouse</div>
      <div class="brand__tags"><span>Cafe | General Store</span><span>Brolga Fuel | Bait | Ice</span></div>
      <div class="brand__contact"><span>Tel.: 6400 1234</span><span>North Yarrow</span></div>
    </header>
    <div class="boards">
      <div class="boards__wood" role="img" aria-label="Weathered timber plank sign"></div>
      <div class="sign">
        <span>Take away food or dine in</span>
        <span>Brolga fuel including premium 98</span>
        <span>Local coffee and tea</span>
        <div class="parking"><span>Off Street</span><span class="parking__of">OF</span><span>Parking</span></div>
        <span>Convenience store</span>
      </div>
    </div>
    <div class="social">Find us on <span class="social__sq"></span>FriendPage</div>
  </section>
</main>
</body>
</html>
```